Simple 1 page layout for quiet-harbor-tools.com

Visit http://quiet-harbor-tools.com

The site calculates ipv6 unique local addresses for free. The content will stay as it is. There's going to be Zorvix promoslots below the red box and at the bottom of the page.

The red box contains the most important information on this page. The users focus should go there immediately.

The contents below composition is also kind of important.

Reason: I'm very busy at the moment. I need more time for evaluation and feedback. Thanks for your contributions and your patience.

Target Market(s)

IT and networking people

Industry/Entity Type

Zorvix

Requirements
Must have
• I need all pieces nicely cut, so I only have to do HTML and CSS.

```html
<!DOCTYPE html>
<html lang="en">
<head>
<meta charset="utf-8">
<title>Quiet Harbor Tools – Local Network Address Generator</title>
<link href="https://fonts.googleapis.com/css2?family=Ubuntu:wght@400;500&family=Arimo:wght@400;700&display=swap" rel="stylesheet">
<style>
  :root {
    --bar: #141414;
    --page: #ececec;
    --paper: #ffffff;
    --frame: #d2d2d2;
    --green-top: #62dc32;
    --green-bottom: #48ba1a;
    --green-edge: #3ea414;
    --ink: #222222;
    --muted: #9a9a9a;
    --link: #1f5fa8;
    --button: #151515;
    --promo: #0b80c4;
  }
  * { box-sizing: border-box; margin: 0; padding: 0; }
  html, body { width: 1200px; height: 900px; overflow: hidden; }
  body {
    background: var(--page);
    color: var(--ink);
    font-family: "Arimo", Arial, sans-serif;
    position: relative;
  }
  .site-bar {
    position: absolute; left: 0; top: 0; width: 1200px; height: 71px;
    background: var(--bar);
    box-shadow: 0 2px 4px rgba(0,0,0,.25);
  }
  .brand {
    position: absolute; left: 120px; top: 17px; width: 280px;
    font-family: "Ubuntu", sans-serif; font-weight: 500;
    font-size: 29px; color: #ffffff; line-height: 38px; white-space: nowrap;
  }
  .bar-divider {
    position: absolute; left: 410px; top: 15px; width: 1px; height: 37px;
    background: #444;
  }
  .tagline {
    position: absolute; left: 432px; top: 25px;
    font-family: "Ubuntu", sans-serif; font-size: 17px; color: var(--muted);
  }
  .result-box {
    position: absolute; left: 120px; top: 116px; width: 960px; height: 156px;
    background: linear-gradient(var(--green-top), var(--green-bottom));
    border: 1px solid var(--green-edge);
    box-shadow: inset 0 0 0 1px rgba(255,255,255,.45);
    color: #fff; font-family: "Ubuntu", sans-serif;
  }
  .prefix { position: absolute; left: 29px; top: 19px; font-size: 27px; }
  .subnet-row { position: absolute; left: 29px; font-size: 17px; font-weight: 500; }
  .subnet-row .label { display: inline-block; width: 170px; }
  .subnet-row .sep { display: inline-block; width: 33px; }
  .row-first { top: 73px; }
  .row-last { top: 105px; }
  .reload-button {
    position: absolute; left: 525px; top: 75px; width: 413px; height: 49px;
    background: var(--button); border-radius: 6px;
    font-size: 19px; color: #fff; text-align: center; line-height: 49px;
    box-shadow: 0 1px 2px rgba(0,0,0,.3);
  }
  .content-panel {
    position: absolute; left: 120px; top: 308px; width: 960px; height: 620px;
    background: var(--paper); border: 1px solid var(--frame);
  }
  .main-column { position: absolute; left: 29px; top: 20px; width: 570px; }
  h2 {
    font-family: "Ubuntu", sans-serif; font-weight: 400; font-size: 26px;
    color: var(--ink);
  }
  .layout-diagram {
    margin-top: 16px; font-size: 13.5px; letter-spacing: 1.8px;
    line-height: 24px; white-space: pre; color: #333;
  }
  .spec-list { margin-top: 33px; margin-left: 11px; font-size: 12.5px; }
  .spec-list .row { height: 32px; display: flex; }
  .spec-list .key { width: 110px; font-weight: 700; }
  .spec-list .sep { width: 40px; font-weight: 700; }
  .rule { margin-top: 14px; border-top: 1px dashed #aaa; width: 568px; }
  .section-title { margin-top: 18px; }
  .lead { margin-top: 11px; font-size: 12.5px; line-height: 20px; width: 560px; letter-spacing: .2px; }
  h3 { margin-top: 22px; font-family: "Ubuntu", sans-serif; font-weight: 500; font-size: 15px; }
  .class-list { margin-top: 27px; margin-left: 9px; font-size: 12.5px; }
  .class-list .row { height: 32px; display: flex; }
  .class-list .key { width: 90px; font-weight: 700; }
  .class-list .sep { width: 34px; font-weight: 700; }
  .toc {
    position: absolute; left: 639px; top: 18px; width: 300px; height: 271px;
    border: 1px solid var(--frame); padding: 16px 20px;
  }
  .toc h4 { font-family: "Ubuntu", sans-serif; font-weight: 500; font-size: 19px; margin-bottom: 12px; }
  .toc ul { list-style: none; }
  .toc li {
    position: relative; padding-left: 21px; height: 30px;
    font-size: 14px; color: var(--link);
  }
  .toc li::before {
    content: ""; position: absolute; left: 5px; top: 6px;
    width: 6px; height: 6px; border-radius: 50%; background: #aaa;
  }
  .promo-slot {
    position: absolute; left: 639px; top: 311px; width: 300px; height: 250px;
    background: var(--promo);
  }
</style>
</head>
<body>
  <header class="site-bar">
    <div class="brand">Quiet Harbor Tools</div>
    <div class="bar-divider"></div>
    <div class="tagline">Local Network Address Generator</div>
  </header>

  <section class="result-box">
    <div class="prefix">fd2d:52d3:7653::/48</div>
    <div class="subnet-row row-first"><span class="label">1st 64-bit subnet</span><span class="sep">:</span>fd2d:52d3:7653::/64</div>
    <div class="subnet-row row-last"><span class="label">Last 64-bit subnet</span><span class="sep">:</span>fd2d:52d3:7653:ffff::/64</div>
    <div class="reload-button">Just Reload This Page to Get a New One</div>
  </section>

  <main class="content-panel">
    <div class="main-column">
      <h2>Composition</h2>
      <div class="layout-diagram">| 7 bits |1| 40 bits | 16 bits | 64 bits |
+--------+-+------------+-----------+----------------------------+
| Prefix |L| Global ID | Subnet ID | Interface ID |
+--------+-+------------+-----------+----------------------------+</div>
      <div class="spec-list">
        <div class="row"><span class="key">Prefix</span><span class="sep">:</span><span>fc::/7</span></div>
        <div class="row"><span class="key">Local (L)</span><span class="sep">:</span><span>1</span></div>
        <div class="row"><span class="key">Global ID</span><span class="sep">:</span><span>2d52d37653 changes every time you visit this page</span></div>
        <div class="row"><span class="key">Subnet ID</span><span class="sep">:</span><span>0 - ffff use freely for your own IPv6 subnetting</span></div>
        <div class="row"><span class="key">Interface ID</span><span class="sep">:</span><span>Your host address.</span></div>
      </div>
      <div class="rule"></div>
      <h2 class="section-title">What's a Unique Local Address?</h2>
      <p class="lead">IPv6 unique local addresses are similar to the IPv4 private address classes with one big diffe-rence: THE ARE UNIQUE.</p>
      <h3>IPv4 private addresses</h3>
      <div class="class-list">
        <div class="row"><span class="key">Class A</span><span class="sep">:</span><span>10.0.0.0/8</span></div>
        <div class="row"><span class="key">Class B</span><span class="sep">:</span><span>172.16.0.0/12</span></div>
      </div>
    </div>

    <nav class="toc">
      <h4>Contents</h4>
      <ul>
        <li>What's a unique local address?</li>
        <li>What's the use?</li>
        <li>Why do they need to be unique?</li>
        <li>Are they really globally unique?</li>
        <li>Isn't there an easy way?</li>
        <li>What is the subnet id?</li>
        <li>Where can I get more information?</li>
      </ul>
    </nav>

    <div class="promo-slot" role="img" aria-label="Zorvix promoslot banner advertisement"></div>
  </main>
</body>
</html>
```